calloway tumbling studio

need a website for above to contain information about the academy, enrollment form etc..

Need a web design for new business Calloway Tumbling Studio offering classes in gymnastics. Info on the business is in the doc called "Web design" which details the tabs I will need on my page. Please see our Facebook page to get an idea of the style Callowaytumblingstudio.

Thank you for your help. I do not require hosting of a domain name just need it all ready to be hosted. Thanks

Budget now increased to include the coding of the website as well.

```html
<!DOCTYPE html>
<html lang="en">
<head>
<meta charset="utf-8">
<title>Calloway Tumbling Studio</title>
<link rel="stylesheet" href="https://fonts.googleapis.com/css2?family=Raleway:wght@600;700&family=Source+Sans+3:wght@300;400;600&family=Arimo:ital,wght@0,400;0,700;1,400&family=Cinzel:wght@600&display=swap">
<style>
:root{
  --ink:#1a1a1a;
  --gold:#e0ac2b;
  --grey-text:#8a8a8a;
  --rule:#cfcfcf;
  --band:#f6f6f6;
  --footer:#9d9d9d;
  --white:#ffffff;
}
*{box-sizing:border-box;margin:0;padding:0}
html,body{width:835px;height:1200px;overflow:hidden;background:var(--white)}
body{font-family:"Arimo",Arial,sans-serif;color:var(--ink)}
.page{position:relative;width:835px;height:1200px;overflow:hidden}
.abs{position:absolute}

.top-rule{left:0;top:0;width:835px;height:4px;background:var(--ink)}
.call-tab{left:428px;top:0;width:338px;height:26px;background:#222;border-radius:0 0 4px 12px;clip-path:polygon(0 0,100% 0,100% 100%,16px 100%);display:flex;align-items:center;padding-left:22px;color:var(--white);gap:6px}
.call-tab .label{font-size:8px;font-weight:700;letter-spacing:.2px}
.call-tab .phone{font-size:12px;letter-spacing:.4px;padding-right:8px;border-right:2px solid var(--white);line-height:14px}
.call-tab .socials{display:flex;gap:6px;margin-left:4px}
.call-tab .socials span{width:15px;height:15px;border-radius:50%;background:var(--white)}

.brand{left:70px;top:18px;font-family:"Raleway",sans-serif;font-weight:700;font-size:21px;line-height:31px;color:var(--ink);letter-spacing:.3px}

.nav{top:76px;left:0;font-family:"Raleway",sans-serif;font-weight:600;font-size:12px;color:#333}
.nav a{position:absolute;color:#333;text-decoration:none;white-space:nowrap}
.nav .active::after{content:"";position:absolute;left:-9px;right:-9px;top:19px;height:3px;background:var(--gold)}
.header-rule{left:0;top:99px;width:835px;height:2px;background:#d8d8d8}

.hero{left:0;top:101px;width:835px;height:333px;background:linear-gradient(100deg,#c4c4c4 0%,#dadada 35%,#a2a2a2 65%,#868686 100%)}
.caption{left:406px;top:169px;width:360px;height:122px;background:rgba(110,110,110,.72);padding:9px 14px}
.caption h1{font-family:"Raleway",sans-serif;font-weight:700;font-size:33px;color:var(--gold);line-height:38px;letter-spacing:.3px}
.caption p{font-family:"Source Sans 3",sans-serif;font-weight:300;font-size:14px;line-height:17px;color:var(--white);margin-top:4px;width:320px}
.dot{top:404px;width:17px;height:17px;border-radius:50%;background:var(--white)}
.dot.current{background:transparent;border:2px solid var(--white)}

.section-title{top:460px;left:0;width:835px;text-align:center;font-family:"Source Sans 3",sans-serif;font-weight:600;font-size:23px;color:var(--gold);letter-spacing:.4px}
.title-rule{top:471px;height:1px;background:#999}
.section-sub{top:494px;left:0;width:835px;text-align:center;font-family:"Source Sans 3",sans-serif;font-size:17px;color:#222}

.class-photo{top:543px;width:328px;height:143px;background:linear-gradient(135deg,#bdbdbd,#7a7a7a 55%,#a8a8a8)}
.col-divider{left:417px;top:542px;height:258px;border-left:1px dashed #bbb}
.coach{top:709px;width:61px;height:61px;background:linear-gradient(160deg,#cfc4bb,#8c7f76)}
.class-name{top:707px;font-size:14px;color:var(--gold)}
.class-text{top:728px;width:256px;font-size:9.6px;line-height:14px;color:var(--grey-text)}
.btn{top:777px;height:20px;padding:0 8px;background:var(--ink);color:var(--white);border-radius:3px;font-size:11px;display:flex;align-items:center;gap:5px}
.btn::after{content:"";border-left:4px solid var(--white);border-top:4px solid transparent;border-bottom:4px solid transparent}

.band{left:0;top:832px;width:835px;height:272px;background:var(--band)}
.band-title{top:846px;font-family:"Cinzel",serif;font-weight:600;font-size:21px;color:#333;letter-spacing:.8px}
.about-lead{left:70px;top:887px;width:378px;font-size:10px;line-height:15.5px;color:var(--gold);text-align:justify}
.about-body{left:70px;top:932px;width:378px;font-size:9px;line-height:14.6px;color:#222;text-align:justify;letter-spacing:.1px}
.band-divider{left:469px;top:854px;height:218px;border-left:1px solid #ddd}

.event{left:490px;width:280px;height:48px}
.date{position:absolute;left:0;top:0;width:40px;height:48px;text-align:center}
.date .day{height:27px;background:#e6e6e6;font-size:17px;line-height:27px;color:#222}
.date .month{height:21px;background:var(--ink);color:var(--white);font-size:13px;line-height:21px}
.event h3{position:absolute;left:52px;top:1px;font-size:10px;font-weight:700;color:var(--gold);letter-spacing:.3px}
.event p{position:absolute;left:52px;top:20px;font-size:8.6px;line-height:14px;color:#222;width:230px}
.event p a{color:var(--gold);font-style:italic;margin-left:8px;text-decoration:underline}

.footer{left:0;top:1104px;width:835px;height:74px;background:var(--footer)}
.foot-link{top:1121px;font-size:12px;color:var(--white)}
.foot-icon{top:1147px;width:13px;height:13px;border-radius:50%;background:var(--white)}
.copyright{left:0;top:1178px;width:835px;height:22px;background:var(--gold);text-align:center;font-size:9px;line-height:22px;color:var(--ink)}
</style>
</head>
<body>
<div class="page">
  <div class="abs top-rule"></div>

  <div class="abs call-tab">
    <svg width="14" height="14" viewBox="0 0 24 24" aria-hidden="true"><path fill="#fff" d="M6.6 10.8a15 15 0 0 0 6.6 6.6l2.2-2.2c.3-.3.7-.4 1-.2 1.1.4 2.3.6 3.6.6.6 0 1 .4 1 1V20c0 .6-.4 1-1 1A17 17 0 0 1 3 4c0-.6.4-1 1-1h3.5c.6 0 1 .4 1 1 0 1.3.2 2.5.6 3.6.1.3 0 .7-.2 1z"/></svg>
    <span class="label">CALL US TODAY</span>
    <span class="phone">865 555-0142</span>
    <div class="socials"><span></span><span></span><span></span><span></span><span></span><span></span></div>
  </div>

  <div class="abs brand">CALLOWAY TUMBLING<br>STUDIO&nbsp; CTS</div>

  <nav class="abs nav">
    <a class="active" style="left:437px">Home</a>
    <a style="left:515px">About us</a>
    <a style="left:609px">Contact Us</a>
    <a style="left:713px">More info</a>
  </nav>
  <div class="abs header-rule"></div>

  <div class="abs hero" role="img" aria-label="Gymnast in a backbend stretch with a class training in the background"></div>
  <div class="abs caption">
    <h1>Lorem ipsum dolor</h1>
    <p>Sed interdum, lacus et vulputate pellentesque, velit nulla&nbsp; ipsum dolor sit amet communitas facilisi congue eu ornare vel, mattis sed eros.</p>
  </div>
  <span class="abs dot current" style="left:685px"></span>
  <span class="abs dot" style="left:715px"></span>
  <span class="abs dot" style="left:746px"></span>

  <div class="abs title-rule" style="left:70px;width:202px"></div>
  <div class="abs title-rule" style="left:563px;width:203px"></div>
  <h2 class="abs section-title">OUR COACHING CLASSES</h2>
  <p class="abs section-sub">Sed ut perspiciatis unde omnis iste natus error sit voluptatem accusantium</p>

  <div class="abs class-photo" style="left:70px" role="img" aria-label="Coach helping young children with floor exercises"></div>
  <div class="abs class-photo" style="left:438px" role="img" aria-label="Gymnasts stretching in splits on mats"></div>
  <div class="abs col-divider"></div>

  <div class="abs coach" style="left:70px" role="img" aria-label="Coach portrait"></div>
  <div class="abs class-name" style="left:144px">Lorem ipsum dolor sit amet</div>
  <p class="abs class-text" style="left:144px">Sed interdum, lacus et vulputate pellentesque, velit nulla ipsum dolor sit amet communitas facilisi congue eu ornare vel, mattis sed eros.</p>
  <a class="abs btn" style="left:144px">Read More</a>

  <div class="abs coach" style="left:438px" role="img" aria-label="Coach portrait"></div>
  <div class="abs class-name" style="left:511px">Lorem ipsum dolor sit amet</div>
  <p class="abs class-text" style="left:511px">Sed interdum, lacus et vulputate pellentesque, velit nulla ipsum dolor sit amet communitas facilisi congue eu ornare vel, mattis sed eros.</p>
  <a class="abs btn" style="left:511px">Read More</a>

  <div class="abs band"></div>
  <h2 class="abs band-title" style="left:70px">About Us</h2>
  <p class="abs about-lead">Sed ut perspiciatis unde omnis iste natus error sit voluptatem accusantium doloremque laudantium, totam rem aperiam,</p>
  <p class="abs about-body">eaque ipsa quae ab illo inventore veritatis et quasi architecto beatae vitae dicta sunt explicabo. Nemo enim ipsam voluptatem quia voluptas sit aspernatur aut odit aut fugit, sed quia consequuntur magni dolores eos qui ratione voluptatem sequi nesciunt. Neque porro quisquam est, qui dolorem ipsum quia dolor sit amet, consectetur, adipisci velit, sed quia non numquam eius modi tempora incidunt ut labore et dolore magnam aliquam quaerat voluptatem. Ut enim ad minima veniam, quis nostrum exercitationem ullam corporis suscipit laboriosam, nisi ut aliquid ex ea commodi consequatur? Quis autem vel eum iure reprehenderit qui in ea voluptate velit esse quam nihil molestiae consequatur, vel illum qui dolorem eum fugiat quo voluptas nulla pariatur</p>
  <div class="abs band-divider"></div>

  <h2 class="abs band-title" style="left:490px">News &amp; Events</h2>
  <div class="abs event" style="top:885px">
    <div class="date"><div class="day">22</div><div class="month">JAN</div></div>
    <h3>Lorem ipsum dolor sit amet,</h3>
    <p>consectetur adipiscing elit, sed do eut laorealiqua. consequat. Duis aute irure dolor. <a>Read More..</a></p>
  </div>
  <div class="abs event" style="top:951px">
    <div class="date"><div class="day">22</div><div class="month">JAN</div></div>
    <h3>Lorem ipsum dolor sit amet,</h3>
    <p>consectetur adipiscing elit, sed do eut laorealiqua. consequat. Duis aute irure dolor. <a>Read More..</a></p>
  </div>
  <div class="abs event" style="top:1018px">
    <div class="date"><div class="day">22</div><div class="month">JAN</div></div>
    <h3>Lorem ipsum dolor sit amet,</h3>
    <p>consectetur adipiscing elit, sed do eut laorealiqua. consequat. Duis aute irure dolor. <a>Read More..</a></p>
  </div>

  <footer class="abs footer"></footer>
  <span class="abs foot-link" style="left:300px">Home</span>
  <span class="abs foot-link" style="left:358px">|</span>
  <span class="abs foot-link" style="left:381px">About us</span>
  <span class="abs foot-link" style="left:454px">|</span>
  <span class="abs foot-link" style="left:477px">Contact Us</span>
  <span class="abs foot-icon" style="left:322px"></span>
  <span class="abs foot-icon" style="left:356px"></span>
  <span class="abs foot-icon" style="left:391px"></span>
  <span class="abs foot-icon" style="left:426px"></span>
  <span class="abs foot-icon" style="left:461px"></span>
  <span class="abs foot-icon" style="left:496px"></span>
  <div class="abs copyright">Copyright © 2014 All Rights Reserved | Privacy Policy</div>
</div>
</body>
</html>
```